Letterhead Design Project

Professional but modern letterhead.

Target Market(s)

mining companies

Industry/Entity Type

It Professional

Colors

Designer to choose colors to be used in the design.

```html
<!DOCTYPE html>
<html lang="en">
<head>
<meta charset="utf-8">
<title>Veyra Letterhead</title>
<link rel="stylesheet" href="https://fonts.googleapis.com/css2?family=Marcellus&family=Open+Sans:wght@400;700&display=swap">
<style>
  :root {
    --brand-blue: #0b3f8c;
    --brand-blue-deep: #082f6e;
    --paper: #ffffff;
    --backdrop: #e9e9ec;
    --faint-mark: #dcdeef;
    --footer-text: #4a4a4a;
  }
  * { margin: 0; padding: 0; box-sizing: border-box; }
  html, body {
    width: 1105px;
    height: 1200px;
    overflow: hidden;
    background: var(--backdrop);
  }
  .canvas {
    position: relative;
    width: 1105px;
    height: 1200px;
  }
  .letterhead {
    position: absolute;
    left: 102px;
    top: 18px;
    width: 900px;
    height: 1164px;
    background: var(--paper);
    box-shadow: 0 2px 10px rgba(0,0,0,0.18);
    overflow: hidden;
  }
  .header-wave {
    position: absolute;
    left: 0;
    top: 0;
    width: 900px;
    height: 141px;
  }
  .website {
    position: absolute;
    right: 56px;
    top: 33px;
    font-family: "Open Sans", sans-serif;
    font-weight: 700;
    font-size: 19px;
    color: var(--paper);
  }
  .brand {
    position: absolute;
    left: 104px;
    top: 150px;
    display: flex;
    align-items: center;
    gap: 16px;
  }
  .brand-dot {
    width: 40px;
    height: 40px;
    border-radius: 50%;
    background: var(--brand-blue);
  }
  .brand-name {
    font-family: "Marcellus", serif;
    font-size: 64px;
    line-height: 1;
    color: var(--brand-blue);
  }
  .brand-watermark {
    position: absolute;
    right: 150px;
    top: 930px;
    font-family: "Marcellus", serif;
    font-size: 130px;
    line-height: 1;
    color: var(--faint-mark);
  }
  .contact-bar {
    position: absolute;
    left: 38px;
    right: 38px;
    top: 1118px;
    display: flex;
    justify-content: space-between;
    font-family: "Open Sans", sans-serif;
    font-size: 13px;
    color: var(--footer-text);
  }
  .contact-group {
    display: flex;
    gap: 14px;
  }
  .contact-item {
    display: flex;
    align-items: center;
    gap: 5px;
  }
  .contact-icon {
    width: 13px;
    height: 13px;
    flex: none;
  }
</style>
</head>
<body>
<div class="canvas">
  <div class="letterhead">
    <svg class="header-wave" viewBox="0 0 512 80" preserveAspectRatio="none" aria-hidden="true">
      <path d="M0,0 H512 V62 C440,70 385,52 300,30 C225,11 140,4 72,16 C40,22 15,38 0,58 Z" fill="var(--brand-blue)"/>
      <path d="M30,22 C110,6 210,10 300,34 C390,58 450,68 512,62" fill="none" stroke="#ffffff" stroke-width="1.6"/>
      <path d="M60,30 C140,14 225,20 305,42 C390,64 450,74 512,68 L512,72 C450,78 388,68 300,46 C220,24 140,20 60,30 Z" fill="var(--brand-blue-deep)"/>
    </svg>
    <div class="website">www.veyradigital.com</div>

    <div class="brand">
      <span class="brand-dot"></span>
      <span class="brand-name">Veyra</span>
    </div>

    <div class="brand-watermark">Veyra</div>

    <div class="contact-bar">
      <div class="contact-group">
        <span class="contact-item">
          <svg class="contact-icon" viewBox="0 0 14 14"><circle cx="7" cy="7" r="7" fill="var(--brand-blue)"/><path d="M4.5,3.5 L6,3.5 L6.6,5.4 L5.7,6.1 C6.2,7.2 6.8,7.8 7.9,8.3 L8.6,7.4 L10.5,8 L10.5,9.5 C7,9.8 4.2,7 4.5,3.5 Z" fill="#fff"/></svg>
          214-555-0182
        </span>
        <span class="contact-item">
          <svg class="contact-icon" viewBox="0 0 14 14"><circle cx="7" cy="7" r="7" fill="var(--brand-blue)"/><rect x="5" y="3" width="4" height="8" rx="0.8" fill="#fff"/></svg>
          214-555-0347
        </span>
        <span class="contact-item">
          <svg class="contact-icon" viewBox="0 0 14 14"><circle cx="7" cy="7" r="7" fill="var(--brand-blue)"/><rect x="3.5" y="5" width="7" height="5" fill="#fff"/><rect x="5" y="3" width="4" height="2" fill="#fff"/></svg>
          214-555-0913
        </span>
        <span class="contact-item">
          <svg class="contact-icon" viewBox="0 0 14 14"><circle cx="7" cy="7" r="7" fill="var(--brand-blue)"/><rect x="3.5" y="4.5" width="7" height="5" fill="#fff"/><path d="M3.5,4.5 L7,7.3 L10.5,4.5" fill="none" stroke="var(--brand-blue)" stroke-width="0.8"/></svg>
          hello@veyradigital.com
        </span>
      </div>
      <span class="contact-item">
        <svg class="contact-icon" viewBox="0 0 14 14"><circle cx="7" cy="7" r="7" fill="var(--brand-blue)"/><path d="M3.5,7 L7,3.8 L10.5,7 L9.5,7 L9.5,10 L4.5,10 L4.5,7 Z" fill="#fff"/></svg>
        Suite # 410, Orr Bldg, Ny 40218
      </span>
    </div>
  </div>
</div>
</body>
</html>
```